Business card - Kite Harbor - size 85 mm * 55 mm

We need new business cards. Design must fit with our vision of the firm. You find in the attached file our logo and a short description of our firm (mission, vision, value, business and so on).

Target Market(s)

Consulting firm in performance improvement

Industry/Entity Type

Management Consulting

Contact Information for Business Card

SIZE
85 mm * 55 mm
INFORMATIONS
name surname
role position
telephone number
email address

Requirements
Must have
• the brand must APPEAR for the rest Would we like to have something sleek, inspired to a "just right" approach
Should not have
• Please avoid the black color as background

```html
<!DOCTYPE html>
<html lang="en">
<head>
<meta charset="UTF-8">
<title>Kite Harbor — Business Card</title>
<link href="https://fonts.googleapis.com/css2?family=Open+Sans:wght@400;600&display=swap" rel="stylesheet">
<style>
  :root {
    --backdrop: #e9e7e4;
    --card-face: #f7f6f5;
    --brand-orange: #ff6a00;
    --band-text: #ffffff;
    --ring-tint: #ff6a00;
  }
  * { box-sizing: border-box; margin: 0; padding: 0; }
  html, body {
    width: 1200px;
    height: 900px;
    overflow: hidden;
    background: var(--backdrop);
    font-family: "Open Sans", sans-serif;
  }
  .canvas {
    width: 1200px;
    height: 900px;
    display: flex;
    align-items: center;
    justify-content: center;
  }
  .business-card {
    width: 880px;
    height: 570px;
    background: var(--card-face);
    display: flex;
    flex-direction: column;
    box-shadow: 0 10px 30px rgba(0,0,0,0.12);
  }
  .brand-area {
    height: 365px;
    display: flex;
    flex-direction: column;
    align-items: center;
    padding-top: 42px;
  }
  .brand-ring {
    width: 196px;
    height: 196px;
  }
  .brand-name {
    margin-top: 30px;
    font-weight: 400;
    font-size: 33px;
    letter-spacing: 0.5em;
    margin-right: -0.5em;
    text-transform: uppercase;
    color: var(--brand-orange);
  }
  .contact-band {
    flex: 1;
    background: var(--brand-orange);
    color: var(--band-text);
    display: flex;
    align-items: center;
    padding-bottom: 14px;
  }
  .person {
    width: 402px;
    text-align: right;
  }
  .person-name {
    font-weight: 600;
    font-size: 28px;
    line-height: 1.15;
  }
  .person-role {
    font-size: 22px;
    line-height: 1.3;
  }
  .contact-list {
    list-style: none;
    margin-left: 40px;
  }
  .contact-item {
    display: flex;
    align-items: center;
    font-size: 22px;
    line-height: 1.45;
  }
  .contact-icon {
    width: 18px;
    height: 18px;
    margin-right: 14px;
    fill: var(--band-text);
  }
</style>
</head>
<body>
<div class="canvas">
  <article class="business-card">
    <header class="brand-area">
      <svg class="brand-ring" viewBox="0 0 200 200" aria-hidden="true">
        <circle cx="100" cy="100" r="88" fill="none" stroke="var(--ring-tint)" stroke-width="9"/>
      </svg>
      <h1 class="brand-name">Kite Harbor</h1>
    </header>
    <section class="contact-band">
      <div class="person">
        <p class="person-name">Daniel Hartwell</p>
        <p class="person-role">Managing Director</p>
      </div>
      <ul class="contact-list">
        <li class="contact-item">
          <svg class="contact-icon" viewBox="0 0 24 24" aria-hidden="true">
            <path d="M6.6 10.8c1.4 2.8 3.8 5.1 6.6 6.6l2.2-2.2c.3-.3.7-.4 1-.2 1.1.4 2.3.6 3.6.6.6 0 1 .4 1 1V20c0 .6-.4 1-1 1C10.6 21 3 13.4 3 4c0-.6.4-1 1-1h3.5c.6 0 1 .4 1 1 0 1.3.2 2.5.6 3.6.1.3 0 .7-.2 1l-2.3 2.2z"/>
          </svg>
          <span>055-482 317 960</span>
        </li>
        <li class="contact-item">
          <svg class="contact-icon" viewBox="0 0 24 24" aria-hidden="true">
            <path d="M3 6h18v12H3z M3 6l9 7 9-7" fill="var(--band-text)" stroke="var(--brand-orange)" stroke-width="1.6" stroke-linejoin="round"/>
          </svg>
          <span>hello@kiteharbor.com</span>
        </li>
      </ul>
    </section>
  </article>
</div>
</body>
</html>
```